Folder Design (inside and out) for a medical technology company

We are a Medical Technology company looking for a professional folder design.
Folder design is for Front, Back, and the flaps inside the folder. We've provided a variety of products at a national level for 20 years, we're targeting a demographic of doctors and are looking to improve out materials.

I attached our logo for reference, please feel free to reach out if you have any questions. Please use the pink and blue logo.

Thank you.

Target Market(s)

Doctors

Industry/Entity Type

Medical, Technology

Requirements
Must have
• Professional design

```html
<!DOCTYPE html>
<html lang="en">
<head>
<meta charset="utf-8">
<title>Novara Medical – Presentation Folder</title>
<link href="https://fonts.googleapis.com/css2?family=Ubuntu:wght@400;500&family=Arimo:wght@400&display=swap" rel="stylesheet">
<style>
  :root{
    --pink:#ef5e8a;
    --pink-deep:#d14a7c;
    --blue:#6a93cd;
    --blue-light:#84b5e4;
    --photo-dark:#3a1420;
    --photo-mid:#8c2a4a;
    --photo-light:#e0608c;
    --ink:#222222;
    --guide-green:#2fa35a;
    --guide-red:#e0405a;
    --guide-blue:#2b3f8f;
    --paper:#ffffff;
  }
  html,body{margin:0;padding:0;}
  body{
    width:1075px;height:1200px;overflow:hidden;
    background:var(--paper);
    position:relative;
  }
  .folder-sheet{position:absolute;top:349px;width:502px;height:502px;}
  .folder-sheet--outside{left:20px;}
  .folder-sheet--inside{left:553px;}
  .brand-name{font-family:'Ubuntu',sans-serif;font-weight:500;fill:var(--blue);}
  .brand-tagline{font-family:'Ubuntu',sans-serif;font-weight:400;fill:var(--pink);}
  .brand-square{fill:var(--pink);}
  .contact-text{font-family:'Arimo',sans-serif;font-size:7px;fill:var(--ink);}
  .contact-icon{fill:var(--pink);}
  .contact-icon-mark{fill:#fff;}
  .guide-safe{fill:none;stroke:var(--guide-green);stroke-width:1.4;stroke-dasharray:4 3;}
  .guide-fold{fill:none;stroke:var(--guide-red);stroke-width:1.2;stroke-dasharray:3 3;}
  .guide-cut{fill:none;stroke:var(--guide-blue);stroke-width:1.6;}
  .guide-bleed{fill:none;stroke:var(--guide-red);stroke-width:1.2;}
</style>
</head>
<body>

<!-- Outside: back cover, front cover and pocket flaps -->
<svg class="folder-sheet folder-sheet--outside" viewBox="0 0 732 732" xmlns="http://www.w3.org/2000/svg">
  <defs>
    <linearGradient id="photoTone" x1="0" y1="0" x2="1" y2="1">
      <stop offset="0" stop-color="var(--photo-dark)"/>
      <stop offset="0.55" stop-color="var(--photo-mid)"/>
      <stop offset="1" stop-color="var(--photo-light)"/>
    </linearGradient>
  </defs>

  <rect class="cover-paper" x="0" y="0" width="732" height="545" fill="var(--paper)"/>

  <!-- header artwork: one pink band over a light blue field -->
  <path class="header-band" d="M0,0 H732 V30 C705,240 560,345 380,345 C220,345 90,285 0,205 Z" fill="var(--pink)"/>
  <path class="header-field" d="M0,0 H560 C520,130 440,255 320,270 C190,285 80,230 0,170 Z" fill="var(--blue-light)"/>
  <path class="cover-photo" role="img" aria-label="Photo of a medical technician in mask and gloves holding a glowing health-icon network, pink tinted"
        d="M400,0 H722 C712,160 640,255 545,258 C448,260 396,160 400,0 Z" fill="url(#photoTone)"/>

  <!-- back cover brand and contacts -->
  <g class="back-brand">
    <rect class="brand-square" x="36" y="482" width="18" height="18"/>
    <text class="brand-name" x="62" y="496" font-size="17">Novara Medical</text>
    <text class="brand-tagline" x="62" y="508" font-size="6">Precision technology for clinicians</text>
  </g>
  <g class="back-contacts">
    <circle class="contact-icon" cx="241" cy="474" r="5"/><circle class="contact-icon-mark" cx="241" cy="474" r="2"/>
    <text class="contact-text" x="253" y="477">www.novaramedical.example</text>
    <circle class="contact-icon" cx="241" cy="493" r="5"/><circle class="contact-icon-mark" cx="241" cy="492" r="1.8"/>
    <text class="contact-text" x="253" y="496">your address here</text>
    <circle class="contact-icon" cx="241" cy="512" r="5"/><rect class="contact-icon-mark" x="239" y="510" width="4" height="4" rx="1"/>
    <text class="contact-text" x="253" y="515">+62 800 1234 5678</text>
  </g>

  <!-- front cover brand and contacts -->
  <g class="front-brand">
    <rect class="brand-square" x="420" y="420" width="34" height="34"/>
    <text class="brand-name" x="466" y="448" font-size="32">Novara Medical</text>
    <text class="brand-tagline" x="466" y="470" font-size="11">Precision technology for clinicians</text>
  </g>
  <g class="front-contacts">
    <circle class="contact-icon" cx="405" cy="522" r="5"/><circle class="contact-icon-mark" cx="405" cy="522" r="2"/>
    <text class="contact-text" x="416" y="525">www.novaramedical.example</text>
    <circle class="contact-icon" cx="521" cy="522" r="5"/><circle class="contact-icon-mark" cx="521" cy="521" r="1.8"/>
    <text class="contact-text" x="532" y="525">your address here</text>
    <circle class="contact-icon" cx="620" cy="522" r="5"/><rect class="contact-icon-mark" x="618" y="520" width="4" height="4" rx="1"/>
    <text class="contact-text" x="631" y="525">+62 800 1234 5678</text>
  </g>

  <!-- pocket flaps -->
  <path class="pocket pocket--left" d="M2,545 L362,545 L340,705 Q336,728 318,728 L2,728 Z" fill="var(--blue)"/>
  <path class="pocket pocket--right" d="M370,545 L732,545 L732,728 L410,728 Q392,728 388,705 Z" fill="var(--pink)"/>

  <!-- production guides -->
  <path class="guide-cut" d="M2,0 L2,728 L318,728 Q336,728 340,705 L366,548 L388,705 Q392,728 410,728 L730,728 L730,0"/>
  <path class="guide-bleed" d="M730,0 L730,728"/>
  <path class="guide-fold" d="M366,345 L366,545 M2,545 L732,545"/>
  <path class="guide-safe" d="M14,12 L14,718 L315,718 Q328,718 331,700 L360,552 M372,552 L398,700 Q401,718 416,718 L718,718 L718,12 L14,12"/>
</svg>

<!-- Inside: spread with pocket flaps -->
<svg class="folder-sheet folder-sheet--inside" viewBox="0 0 732 732" xmlns="http://www.w3.org/2000/svg">
  <rect class="cover-paper" x="0" y="0" width="732" height="545" fill="var(--paper)"/>

  <path class="inner-band-pink" d="M4,250 L4,300 C180,310 340,170 363,0 L355,0 C330,150 180,270 4,250 Z" fill="var(--pink)"/>
  <path class="inner-band-blue" d="M4,245 L4,282 C180,290 330,160 358,0 L352,0 C322,150 175,262 4,245 Z" fill="var(--blue)"/>

  <g class="inside-brand">
    <rect class="brand-square" x="46" y="58" width="28" height="28"/>
    <text class="brand-name" x="84" y="82" font-size="25">Novara Medical</text>
    <text class="brand-tagline" x="84" y="100" font-size="9">Precision technology for clinicians</text>
  </g>

  <path class="pocket pocket--left" d="M2,545 L358,545 L336,705 Q332,728 314,728 L2,728 Z" fill="var(--pink)"/>
  <path class="pocket pocket--right" d="M370,545 L730,545 L730,728 L406,728 Q388,728 384,705 Z" fill="var(--blue)"/>

  <g class="card-slits" stroke="var(--guide-blue)" stroke-width="2">
    <line x1="98" y1="612" x2="128" y2="582"/>
    <line x1="250" y1="582" x2="280" y2="612"/>
    <line x1="98" y1="658" x2="128" y2="688"/>
    <line x1="250" y1="688" x2="280" y2="658"/>
  </g>

  <path class="guide-cut" d="M2,0 L730,0 L730,728 L406,728 Q388,728 384,705 L364,550 L340,705 Q336,728 318,728 L2,728 Z"/>
  <path class="guide-bleed" d="M6,4 L726,4 L726,724 M6,4 L6,724"/>
  <path class="guide-fold" d="M364,0 L364,545 M2,545 L730,545"/>
  <path class="guide-safe" d="M12,12 L720,12 L720,718 L410,718 Q396,718 393,700 L368,552 M360,552 L334,700 Q331,718 316,718 L12,718 L12,12"/>
</svg>

</body>
</html>
```